Book Cover for Cyber Compliance Book

I need to get a book cover designed for use on "Pagewell Print Portal" - template attached.

The name of the book is: Charting KELMOR

Tagline: A Boardroom Leader’s Field Guide to Oversight and Endurance

Author: Martin J Hollis

Photo of author is attached and a logo for the QBWLN publishing organisation.

Please note: the author is high profile in the cyber security industry and use of his image and name on the book will help online sales.

I am open to changing the amount of copy used on the front and back of the book.

The book is about a European regulation for the financial sector called DORA Digital Operational Resilience Act. It is aimed at corporate level executives within the financial sector and the imagery should include relevant elements such as the EU, Financial sector, digital operations and cybersecurity.

I want to find an imaginative designer than can create something special and appealing.

I am not clear on exactly how many pages will be in the book so the template details may change slightly as the number becomes clear for the width of the spine etc. I will require all the template files used so I can make minor edits in AI or Photoshop

Note I can get the photo and attached logo in higher resolution if required

If possible I would like to see a 3D mockup of the book

Synopsis of Book:

n the ever-evolving landscape of financial services, the Digital Operational Resilience Act (DORA) stands as a beacon of change, ushering in a new era of regulatory requirements aimed at fortifying the digital fortitude of the sector. “Charting KELMOR: A Boardroom Leader’s Field Guide to Oversight and Endurance” is an indispensable guide tailored for leaders who are steering their organisations through the complexities of DORA compliance.
This comprehensive manual delves into the intricacies of DORA, elucidating the rationale behind its inception – the need for a unified and robust approach to managing ICT risks that have become increasingly prevalent in today’s interconnected financial ecosystem. The book offers a granular analysis of the five pillars central to DORA: ICT Risk Management, ICT-related Incident Management, Digital Operational Resilience Testing, ICT Third Party Risk Management, and Information Sharing Arrangements.
For financial entities and ICT service providers operating within the EU and beyond, “Charting KELMOR” serves as a strategic compass. It provides actionable insights into aligning with DORA’s standards, ensuring not just compliance but also a competitive edge in the EU market. The guide highlights the strategic importance of continuous learning and the emergence of specialized roles such as DORA Compliance Specialists, addressing the skills gap and career opportunities within this new regulatory framework.
The book also offers a detailed walkthrough of the Union-wide Oversight Framework, a novel aspect of DORA that places critical ICT third-party providers under direct regulatory scrutiny. It outlines the necessary steps for financial entities to ensure seamless collaboration with these providers, including the integration of specific contractual obligations to uphold DORA’s stringent resilience standards.
With practical advice and real-world scenarios, “Charting KELMOR” equips executives with the knowledge to conduct thorough DORA Compliance Assessments, map dependencies, and engage in scenario testing that aligns with the act’s rigorous testing regimen. It is not just a guide but a strategic tool for proactive adaptation and evolution in the face of DORA’s demands.
As the financial sector navigates these new regulatory waters, “Charting KELMOR” emerges as the quintessential guide for those committed to not just surviving but thriving in the age of digital operational resilience. It is a clarion call for attentiveness, alignment, and preparedness – a must-read for every financial service executive determined to lead their organization with foresight and fortitude.

```html
<!DOCTYPE html>
<html lang="en">
<head>
<meta charset="utf-8">
<title>Charting KELMOR — Front Cover</title>
<link href="https://fonts.googleapis.com/css2?family=Montserrat:wght@500;600;700;800&display=swap" rel="stylesheet">
<style>
  :root {
    --stage: #141414;
    --navy-deep: #0c1c2c;
    --navy: #16324a;
    --navy-mid: #1d4058;
    --teal-glow: #2f8f9a;
    --teal-soft: #1b5565;
    --amber: #f5a72a;
    --white: #ffffff;
    --band-blue: #1f62b3;
    --suit-dark: #1c232c;
  }
  * { margin: 0; padding: 0; box-sizing: border-box; }
  html, body {
    width: 1200px;
    height: 1200px;
    overflow: hidden;
    background: var(--stage);
  }
  .canvas {
    position: relative;
    width: 1200px;
    height: 1200px;
    display: flex;
    align-items: center;
    justify-content: center;
  }
  .cover {
    position: relative;
    width: 734px;
    height: 1100px;
    overflow: hidden;
    background: linear-gradient(160deg, var(--navy) 0%, var(--navy-deep) 55%, var(--navy-mid) 100%);
    font-family: "Montserrat", sans-serif;
  }
  .market-visual {
    position: absolute;
    left: 290px;
    top: 330px;
    width: 444px;
    height: 470px;
    background:
      radial-gradient(ellipse at 60% 40%, rgba(80, 200, 210, 0.45) 0%, rgba(47, 143, 154, 0.2) 40%, transparent 70%),
      linear-gradient(180deg, transparent 0%, var(--teal-soft) 45%, transparent 100%);
  }
  .trend-line {
    position: absolute;
    left: 160px;
    top: 300px;
    width: 574px;
    height: 320px;
  }
  .title {
    position: absolute;
    left: 0;
    top: 70px;
    width: 100%;
    text-align: center;
    line-height: 1;
  }
  .title-lead {
    display: block;
    color: var(--amber);
    font-weight: 700;
    font-size: 96px;
    letter-spacing: -1px;
  }
  .title-main {
    display: block;
    margin-top: 12px;
    color: var(--white);
    font-weight: 800;
    font-size: 138px;
    letter-spacing: 2px;
  }
  .author-portrait {
    position: absolute;
    left: 0;
    top: 380px;
    width: 350px;
    height: 720px;
    background: linear-gradient(180deg, rgba(28, 35, 44, 0) 0%, rgba(28, 35, 44, 0.55) 30%, var(--suit-dark) 60%, #121820 100%);
  }
  .tagline {
    position: absolute;
    left: 336px;
    top: 640px;
    width: 380px;
    color: var(--white);
    font-weight: 500;
    font-size: 31px;
    line-height: 1.22;
  }
  .author-band {
    position: absolute;
    left: 338px;
    top: 878px;
    width: 396px;
    height: 66px;
    background: var(--band-blue);
    display: flex;
    align-items: center;
    padding-left: 34px;
  }
  .author-name {
    color: var(--white);
    font-weight: 700;
    font-size: 34px;
  }
</style>
</head>
<body>
  <main class="canvas">
    <section class="cover">
      <div class="market-visual" role="img" aria-label="Glowing financial market chart with a hand touching a rising data point"></div>
      <svg class="trend-line" viewBox="0 0 574 320" aria-hidden="true">
        <polyline points="0,250 60,225 120,205 180,180 240,150 300,130 360,110 420,80 470,50 520,20"
                  fill="none" stroke="#5fd3d6" stroke-width="3" opacity="0.85"/>
        <circle cx="520" cy="20" r="7" fill="#dff9fb"/>
      </svg>

      <h1 class="title">
        <span class="title-lead">Charting</span>
        <span class="title-main">KELMOR</span>
      </h1>

      <div class="author-portrait" role="img" aria-label="Portrait of the author in a dark suit and pink tie"></div>

      <p class="tagline">A Boardroom Leader’s Field Guide to Oversight and Endurance</p>

      <div class="author-band">
        <span class="author-name">Martin J Hollis</span>
      </div>
    </section>
  </main>
</body>
</html>
```